Supplement Bottle Packaging and Design

We want to rebrand our current health supplements (see below). We do want it to be modern, vibrant and appealing supplement bottles. Very upscale and elegant as it targets primarily women.
NOTE: READ THE ATTACHED WORD DOCUMENT!
Bottle size: We are totally open to the bottle size and shape, as long it's a typical supplement bottle size to handle 90-120 capsules; what we mostly need is new bottle design/packaging. YOU DON’T HAVE TO USE THE CURRENT WHITE BOTTLE SHAPE, BUT ANYTHING MORE MODERN WOULD WORK!
Updates
We need more modern, clean sleek designs to choose from
Look and feel
Each slider illustrates characteristics of the customer's brand and the style your logo design should communicate.

```html
<!DOCTYPE html>
<html lang="en">
<head>
<meta charset="utf-8">
<title>Velmora Supplement Labels</title>
<link rel="stylesheet" href="https://fonts.googleapis.com/css2?family=Krona+One&family=Lexend+Exa:wght@400;500;600&display=swap">
<style>
  :root {
    --canvas: #ffffff;
    --ink: #ffffff;
    --green-a: #1d7f1f; --green-b: #2fa036;
    --blue-a: #0a0cf5; --blue-b: #2c3cff;
    --purple-a: #6a22b0; --purple-b: #b036ff;
    --red-a: #a81414; --red-b: #ff1e1e;
    --band: rgba(255,255,255,0.5);
  }
  html, body {
    margin: 0; padding: 0;
    width: 1200px; height: 810px;
    overflow: hidden;
    background: var(--canvas);
  }
  .shelf {
    position: relative;
    width: 1200px; height: 810px;
  }
  .label {
    position: absolute;
    top: 386px;
    width: 222px; height: 265px;
    overflow: hidden;
  }
  .label svg { display: block; }
  .label--hormone { left: 94px; }
  .label--blood { left: 359px; }
  .label--liver { left: 624px; }
  .label--tummy { left: 888px; }

  .title { font-family: "Krona One", sans-serif; fill: var(--ink); }
  .sub { font-family: "Lexend Exa", sans-serif; fill: var(--ink); font-weight: 400; }
  .sub--small { font-weight: 500; }
  .meta { font-family: "Lexend Exa", sans-serif; fill: var(--ink); font-weight: 500; }
  .count { font-family: "Krona One", sans-serif; fill: var(--ink); }
</style>
</head>
<body>
<main class="shelf">

  <div class="label label--hormone">
    <svg width="222" height="265" viewBox="0 0 222 265">
      <defs>
        <linearGradient id="g-hormone" x1="0" x2="1" y1="0" y2="0">
          <stop offset="0" stop-color="var(--green-a)"/>
          <stop offset="1" stop-color="var(--green-b)"/>
        </linearGradient>
      </defs>
      <rect width="222" height="265" fill="url(#g-hormone)"/>
      <path class="band" d="M0,8 Q111,80 222,8 L222,39 Q111,91 0,39 Z" fill="var(--band)"/>
      <text class="title" x="111" y="104" text-anchor="middle" font-size="31" textLength="204" lengthAdjust="spacing">Hormone</text>
      <text class="title" x="111" y="125" text-anchor="middle" font-size="17" textLength="140" lengthAdjust="spacing">Velmora</text>
      <text class="sub" x="111" y="145" text-anchor="middle" font-size="12.5" textLength="180" lengthAdjust="spacing">Supports Healthy</text>
      <text class="sub sub--small" x="111" y="157" text-anchor="middle" font-size="10" textLength="138" lengthAdjust="spacing">Hormone Levels</text>
      <text class="meta" x="111" y="172" text-anchor="middle" font-size="7.5" textLength="108" lengthAdjust="spacing">Dietary Supplement</text>
      <text class="count" x="111" y="232" text-anchor="middle" font-size="11">60</text>
      <text class="meta" x="111" y="242" text-anchor="middle" font-size="9" textLength="131" lengthAdjust="spacing">Vegetable Capsules</text>
    </svg>
  </div>

  <div class="label label--blood">
    <svg width="222" height="265" viewBox="0 0 222 265">
      <defs>
        <linearGradient id="g-blood" x1="0" x2="1" y1="0" y2="0">
          <stop offset="0" stop-color="var(--blue-b)"/>
          <stop offset="0.5" stop-color="var(--blue-a)"/>
          <stop offset="1" stop-color="var(--blue-b)"/>
        </linearGradient>
      </defs>
      <rect width="222" height="265" fill="url(#g-blood)"/>
      <path class="band" d="M0,8 Q111,80 222,8 L222,39 Q111,91 0,39 Z" fill="var(--band)"/>
      <text class="title" x="111" y="106" text-anchor="middle" font-size="40" textLength="201" lengthAdjust="spacing">Blood</text>
      <text class="title" x="111" y="126" text-anchor="middle" font-size="14" textLength="190" lengthAdjust="spacing">Sugar Velmora</text>
      <text class="sub" x="111" y="150" text-anchor="middle" font-size="12.5" textLength="172" lengthAdjust="spacing">Supports Healthy</text>
      <text class="sub sub--small" x="111" y="161" text-anchor="middle" font-size="9" textLength="153" lengthAdjust="spacing">Blood Glucose Levels</text>
      <text class="meta" x="111" y="175" text-anchor="middle" font-size="7.5" textLength="119" lengthAdjust="spacing">Dietary Supplement</text>
      <text class="count" x="111" y="232" text-anchor="middle" font-size="11">60</text>
      <text class="meta" x="111" y="242" text-anchor="middle" font-size="9" textLength="131" lengthAdjust="spacing">Vegetable Capsules</text>
    </svg>
  </div>

  <div class="label label--liver">
    <svg width="222" height="265" viewBox="0 0 222 265">
      <defs>
        <linearGradient id="g-liver" x1="0" x2="1" y1="0" y2="0">
          <stop offset="0" stop-color="var(--purple-a)"/>
          <stop offset="1" stop-color="var(--purple-b)"/>
        </linearGradient>
      </defs>
      <rect width="222" height="265" fill="url(#g-liver)"/>
      <path class="band" d="M0,8 Q111,80 222,8 L222,39 Q111,91 0,39 Z" fill="var(--band)"/>
      <text class="title" x="111" y="109" text-anchor="middle" font-size="40" textLength="197" lengthAdjust="spacing">Liver</text>
      <text class="title" x="111" y="138" text-anchor="middle" font-size="22" textLength="170" lengthAdjust="spacing">Velmora</text>
      <text class="sub" x="111" y="158" text-anchor="middle" font-size="14" textLength="156" lengthAdjust="spacing">Rejuvenating</text>
      <text class="sub sub--small" x="111" y="168" text-anchor="middle" font-size="7" textLength="136" lengthAdjust="spacing">Cleanse &amp; Detox Formula</text>
      <text class="meta" x="111" y="180" text-anchor="middle" font-size="8" textLength="119" lengthAdjust="spacing">Dietary Supplement</text>
      <text class="count" x="111" y="232" text-anchor="middle" font-size="11">120</text>
      <text class="meta" x="111" y="242" text-anchor="middle" font-size="9" textLength="131" lengthAdjust="spacing">Vegetable Capsules</text>
    </svg>
  </div>

  <div class="label label--tummy">
    <svg width="222" height="265" viewBox="0 0 222 265">
      <defs>
        <linearGradient id="g-tummy" x1="0" x2="1" y1="0" y2="0">
          <stop offset="0" stop-color="var(--red-a)"/>
          <stop offset="1" stop-color="var(--red-b)"/>
        </linearGradient>
      </defs>
      <rect width="222" height="265" fill="url(#g-tummy)"/>
      <path class="band" d="M0,8 Q111,80 222,8 L222,39 Q111,91 0,39 Z" fill="var(--band)"/>
      <text class="title" x="111" y="104" text-anchor="middle" font-size="33" textLength="202" lengthAdjust="spacing">Tummy</text>
      <text class="title" x="111" y="125" text-anchor="middle" font-size="17" textLength="140" lengthAdjust="spacing">Velmora</text>
      <text class="sub" x="111" y="147" text-anchor="middle" font-size="14" textLength="156" lengthAdjust="spacing">Oxygenating</text>
      <text class="sub sub--small" x="111" y="158" text-anchor="middle" font-size="10.5" textLength="125" lengthAdjust="spacing">Colon Cleanse</text>
      <text class="meta" x="111" y="171" text-anchor="middle" font-size="7.5" textLength="108" lengthAdjust="spacing">Dietary Supplement</text>
      <text class="count" x="111" y="232" text-anchor="middle" font-size="11">90</text>
      <text class="meta" x="111" y="242" text-anchor="middle" font-size="9" textLength="131" lengthAdjust="spacing">Vegetable Capsules</text>
    </svg>
  </div>

</main>
</body>
</html>
```